SImple & Cool Baby Sling Wrap Box Packaging Design

Looking for a packaging design for our Baby Sling Wrap product.

Plume Co. is a premier manufacturer and marketer of baby products. Our products are sold through retailers and online stores.

We are looking for a packaging design for our Baby Sling Wrap

Box Packaging Size
Height: 3 inches
Width: 6.5 inches
Length: 13.5 inches
Packaging Window: 2inches Height x 2inches Diameter. (please see attachment for example)

Features: (May be re-worded)
-Breathable 95% Cotton 5% Stretchy Spandex
-Safety & Durable
-One Size Fits All
-Hands Free

Packaging Requirements
**Should contain a stork with the window hole as the bag.**
**Step by step instructions on the back of packaging**
**"Swaddle wrap" similar text (see attachment) must say "Baby Sling Wrap for main front packaging, top of box"**
**logo on the side of box**

Eco-friendly Brown Box
Color Scheme: 1 primary color, white, dark grey, brown box color as background.

Target Market(s)

-First time Parents
-Mothers
-Moms
-Parents
-Grandparents

Industry/Entity Type

Baby Care

Colors
ffffff
000000
b2b2b2

Requirements
Must have
• Packaging Requirements
• **Should contain a stork with the window hole as the bag.**
• **Step by step instructions on the back of packaging**
• **"Swaddle wrap" similar text (see attachment) must say "Baby Sling Wrap for main front packaging, top of box"**
• **logo on the side of box**
Nice to have
• Eco-friendly Brown Box
• Color Scheme: 1-2 primary color, white, dark grey, brown box color as background.
• -Warm child feeling
• -Cartoon
Should not have
• No human characters
• Not too many colors

```html
<!DOCTYPE html>
<html lang="en">
<head>
<meta charset="utf-8">
<title>Baby Sling Wrap – Box Packaging</title>
<link href="https://fonts.googleapis.com/css2?family=Lobster&family=Open+Sans:wght@400;600&display=swap" rel="stylesheet">
<style>
  :root {
    --stage: #d4d4d4;
    --box-brown: #4b3a35;
    --box-brown-dark: #3c2e2a;
    --tab-brown: #6f5e58;
    --window-dark: #241a17;
    --window-ring: #5d4a44;
    --white: #ffffff;
    --soft-grey: #b2b2b2;
    --ink: #000000;
  }
  * { box-sizing: border-box; margin: 0; padding: 0; }
  html, body {
    width: 1200px; height: 787px; overflow: hidden;
    background: var(--stage);
  }
  .canvas { position: relative; width: 1200px; height: 787px; }

  .side-panel {
    position: absolute; left: 75px; top: 186px;
    width: 191px; height: 414px;
    background: var(--box-brown-dark);
    display: flex; align-items: center; justify-content: center;
    border-right: 1px solid rgba(255,255,255,0.08);
  }
  .side-panel .brand-mark {
    display: flex; align-items: center; gap: 8px;
    font-family: "Lobster", cursive;
    font-size: 26px; color: var(--white);
  }
  .brand-mark .dot {
    width: 12px; height: 12px; border-radius: 50%;
    background: var(--white);
  }

  .top-face {
    position: absolute; left: 266px; top: 186px;
    width: 860px; height: 414px;
    background: var(--box-brown);
    overflow: hidden;
  }
  .product-title {
    position: absolute; left: 44px; top: 58px;
    font-family: "Lobster", cursive;
    font-size: 54px; color: var(--white);
    letter-spacing: 1px;
  }
  .stork-art {
    position: absolute; left: 520px; top: 36px;
    width: 320px; height: 190px;
    border-radius: 40px;
    background: linear-gradient(135deg, #f4f1ef 0%, #d9d2ce 60%, #8b7872 100%);
  }
  .bag-window {
    position: absolute; left: 260px; top: 175px;
  }
  .features-tab {
    position: absolute; left: 30px; top: 265px;
    width: 190px; height: 32px;
    background: var(--tab-brown);
    border-radius: 0 8px 8px 0;
    padding-left: 14px;
    font-family: "Lobster", cursive;
    font-size: 22px; line-height: 32px; color: var(--white);
  }
  .feature-list {
    position: absolute; left: 40px; top: 308px;
    list-style: none;
    font-family: "Open Sans", sans-serif;
    font-size: 14px; line-height: 18px; color: var(--white);
  }
  .feature-list li { position: relative; padding-left: 14px; }
  .feature-list li::before {
    content: ""; position: absolute; left: 0; top: 6px;
    width: 6px; height: 6px; border-radius: 50%;
    background: var(--white);
  }
  .feature-list li.continued::before { display: none; }
</style>
</head>
<body>
<main class="canvas">
  <section class="side-panel" aria-label="Box side">
    <div class="brand-mark"><span class="dot"></span>Plume Co.</div>
  </section>

  <section class="top-face" aria-label="Box top">
    <h1 class="product-title">Baby Sling Wrap</h1>

    <div class="stork-art" role="img" aria-label="Cartoon stork flying, carrying the window as its bag"></div>

    <svg class="bag-window" width="150" height="150" viewBox="0 0 150 150" aria-label="Product window">
      <circle cx="75" cy="75" r="74" fill="var(--window-ring)"/>
      <circle cx="75" cy="78" r="64" fill="var(--window-dark)"/>
    </svg>

    <div class="features-tab">Features:</div>
    <ul class="feature-list">
      <li>Breathable 95% Cotton</li>
      <li class="continued">5% Stretchy Spandex</li>
      <li>Safety &amp; Durable</li>
      <li>One Size Fits All</li>
      <li>Hands Free</li>
    </ul>
  </section>
</main>
</body>
</html>
```